PowerPoint Template Design for Quarry Lending

Design a PowerPoint template for Quarry Lending, tailored for presentations to sophisticated mortgage servicing investors. The template should reflect a high level of professionalism, with a clean and modern aesthetic that resonates with an informed and discerning audience. The design must effectively integrate Quarry Lending's branding elements, ensuring a coherent visual narrative that reinforces our reputation for expertise and reliability in the mortgage servicing sector.

```html
<!DOCTYPE html>
<html lang="en">
<head>
<meta charset="utf-8">
<title>Quarry Lending – Mortgage Servicing Investor Template</title>
<link href="https://fonts.googleapis.com/css2?family=Roboto:wght@400;500;700;900&display=swap" rel="stylesheet">
<style>
:root{
  --navy:#15284f;
  --gold:#d6a534;
  --teal:#36aaa2;
  --stage:#a9c5c6;
  --white:#ffffff;
  --ink:#1b1f2a;
  --muted:#8b8f98;
}
*{box-sizing:border-box;margin:0;padding:0}
html,body{width:1200px;height:3694px;overflow:hidden}
body{background:var(--stage);font-family:"Roboto",Arial,sans-serif;color:var(--ink);position:relative}

/* showcase band */
.showcase{position:absolute;left:0;top:108px;width:1200px;height:798px;overflow:hidden;background:#dfe6ea}
.showcase-grid{position:absolute;left:-420px;top:-520px;width:2100px;display:grid;grid-template-columns:repeat(7,290px);gap:10px;transform:rotate(-30deg);transform-origin:center}
.tile{height:165px;background:var(--white);position:relative;overflow:hidden}
.tile .blk{position:absolute;background:var(--navy)}
.tile .pic{position:absolute;background:linear-gradient(135deg,#9fb3c4,#5e6f82)}
.tile h4{position:absolute;left:22px;top:60px;font-size:17px;font-weight:700;line-height:1.15;color:var(--navy)}
.tile h4 em{font-style:normal;color:var(--gold);display:block}

/* slides */
.slide{position:absolute;width:570px;height:320px;background:var(--white);overflow:hidden}
.col-l{left:29px}.col-r{left:619px}
.abs{position:absolute}
.navy{background:var(--navy)}
.teal{background:var(--teal)}
.photo{position:absolute;background:linear-gradient(140deg,#c9d3dc,#7d8b99)}
.photo.warm{background:linear-gradient(140deg,#d9c7b2,#8a6a52)}
.photo.sky{background:linear-gradient(160deg,#b9d0e6,#4c6b91)}
.photo.desk{background:linear-gradient(140deg,#e6e6e4,#9aa0a6)}
.photo.green{background:linear-gradient(180deg,#dfe9ef 0%,#c7b58f 55%,#6f8f3c 100%)}
.photo.red{background:linear-gradient(140deg,#4a4f5a,#a33a2e)}
.brand-tag{position:absolute;left:18px;top:14px;font-size:7px;font-weight:700;color:var(--navy);padding-left:6px;border-left:2px solid var(--gold);line-height:9px}
.brand-tag.on-navy{color:var(--white)}
.menu{position:absolute;right:14px;top:12px;width:11px;height:9px}
.foot-brand{position:absolute;right:14px;bottom:10px;font-size:7px;font-weight:700;color:var(--gold)}
.kicker{font-size:7px;color:var(--muted);margin-bottom:6px}
.title{font-size:19px;font-weight:700;line-height:1.2;color:var(--navy)}
.title .gold{color:var(--gold)}
.on-dark .title,.on-dark{color:var(--white)}
.body{font-size:6.5px;line-height:1.6;color:var(--muted)}
.on-dark .body{color:#c9d0de}
.btn{display:inline-block;margin-top:12px;background:var(--teal);color:var(--white);font-size:6px;padding:4px 12px}
.stat{font-size:14px;font-weight:700}
.stat small{display:block;font-size:5.5px;font-weight:400;color:var(--muted);margin-top:3px}
.tick{display:flex;align-items:center;gap:6px;font-size:6.5px;font-weight:700;color:var(--white);margin-top:8px}
.card{position:absolute;padding:12px 14px;font-size:6.5px;line-height:1.6}
.card b{display:block;font-size:7px;margin-bottom:3px}
.stars{color:var(--teal);font-size:9px;letter-spacing:1px}
.svc{position:absolute;left:244px;width:150px}
.svc b{font-size:7px;color:var(--navy);display:block;margin-bottom:3px}
.svc-ico{position:absolute;left:194px;width:24px;height:24px;background:var(--teal);display:flex;align-items:center;justify-content:center}
.contact{font-size:7px;color:var(--navy);display:flex;gap:12px;margin-bottom:10px;align-items:flex-start}
.contact b{display:block}
.contact span{color:var(--muted);font-size:6px}
</style>
</head>
<body>

<!-- showcase collage -->
<section class="showcase" role="img" aria-label="Angled overview of the template slides">
  <div class="showcase-grid">
    <div class="tile"><div class="blk" style="right:0;top:0;width:110px;height:120px"></div><h4>What We<em>Service</em></h4></div>
    <div class="tile"><h4>Thanks</h4><div class="pic" style="right:0;top:20px;width:130px;height:110px"></div></div>
    <div class="tile"><div class="pic" style="left:0;top:0;width:100%;height:70px"></div><div class="blk" style="left:0;top:70px;width:130px;height:95px"></div></div>
    <div class="tile"><h4>Greetings and<em style="color:var(--navy)">Agenda</em></h4><div class="blk" style="right:0;top:0;width:90px;height:110px"></div></div>
    <div class="tile"><div class="pic" style="right:0;top:0;width:140px;height:165px"></div><h4><em>Types of Mortgage</em>Servicing Investments</h4></div>
    <div class="tile"><div class="blk" style="left:0;top:0;width:100%;height:165px"></div></div>
    <div class="tile"><h4>Thanks</h4></div>

    <div class="tile"><div class="pic" style="left:0;top:0;width:150px;height:165px"></div><h4 style="left:165px"><em>Shaping</em>the Future</h4></div>
    <div class="tile"><h4>Unlocking Value in<em>Mortgage Servicing</em></h4><div class="blk" style="left:0;bottom:0;width:100%;height:40px"></div></div>
    <div class="tile"><div class="pic" style="left:0;top:0;width:100%;height:165px"></div></div>
    <div class="tile"><h4><em>Investment</em>Opportunities</h4><div class="pic" style="left:0;top:0;width:100px;height:80px"></div></div>
    <div class="tile"><div class="pic" style="left:0;top:0;width:100%;height:80px"></div><div class="blk" style="left:0;top:80px;width:150px;height:85px"></div></div>
    <div class="tile"><h4><em>Unlocking</em>Mortgage</h4></div>
    <div class="tile"><div class="blk" style="left:0;top:0;width:100%;height:165px"></div></div>

    <div class="tile"><div class="blk" style="left:0;top:0;width:120px;height:165px"></div><div class="pic" style="right:0;top:0;width:140px;height:165px"></div></div>
    <div class="tile"><h4><em>Economic</em>Influencers</h4></div>
    <div class="tile"><div class="pic warm" style="left:0;top:0;width:100%;height:165px"></div></div>
    <div class="tile"><h4><em>Risks and</em>Mitigations</h4><div class="blk" style="left:0;bottom:0;width:100%;height:35px"></div></div>
    <div class="tile"><div class="blk" style="left:0;top:0;width:100%;height:165px"></div></div>
    <div class="tile"><h4><em>Key Players in</em>Mortgage Servicing</h4></div>
    <div class="tile"><div class="pic" style="left:0;top:0;width:100%;height:165px"></div></div>

    <div class="tile"><div class="blk" style="left:0;top:0;width:100%;height:165px"></div></div>
    <div class="tile"><h4><em>Key Players in</em>Mortgage Servicing</h4><div class="blk" style="left:0;bottom:0;width:220px;height:55px"></div></div>
    <div class="tile"><div class="pic warm" style="left:0;top:0;width:100%;height:165px"></div></div>
    <div class="tile"><h4><em>Market Trends</em>and Outlook</h4></div>
    <div class="tile"><div class="blk" style="left:0;top:0;width:100%;height:165px"></div></div>
    <div class="tile"><h4>Thanks</h4></div>
    <div class="tile"><div class="pic" style="left:0;top:0;width:100%;height:165px"></div></div>
  </div>
</section>

<!-- Slide 1: cover -->
<section class="slide col-l" style="top:922px">
  <div class="abs" style="left:50px;top:36px;font-size:16px;font-weight:700;color:var(--navy)">Quarry Lending</div>
  <div class="photo warm" style="left:280px;top:30px;width:280px;height:222px" role="img" aria-label="Model house with red roof beside a calculator and pen"></div>
  <div class="abs navy" style="left:0;top:236px;width:570px;height:84px"></div>
  <div class="abs teal" style="left:0;top:122px;width:29px;height:122px"></div>
  <div class="abs" style="left:29px;top:122px;width:240px;height:122px;background:var(--white);padding:18px 20px">
    <div class="kicker">Live Better, Mortgage Smarter</div>
    <div class="title">Unlocking Value in<br><span class="gold">Mortgage Servicing<br>Investments</span></div>
  </div>
  <div class="abs" style="right:24px;bottom:20px;font-size:6px;color:var(--white)">Start Slide &#8250;</div>
</section>

<!-- Slide 2: agenda -->
<section class="slide col-r" style="top:922px">
  <div class="abs navy" style="left:344px;top:0;width:226px;height:236px"></div>
  <div class="brand-tag">Quarry Lending</div>
  <svg class="menu" viewBox="0 0 11 9"><path d="M0 1h11M0 4.5h11M0 8h11" stroke="#fff" stroke-width="1"/></svg>
  <div class="abs" style="left:57px;top:86px;width:200px">
    <div class="kicker">Introduction</div>
    <div class="title"><span class="gold">Greetings and</span><br>Agenda</div>
    <p class="body" style="margin-top:14px">A short overview of who we are, what this deck covers and how our servicing portfolio delivers steady value for investors.</p>
    <span class="btn">Read More</span>
  </div>
  <div class="photo desk" style="left:262px;top:75px;width:227px;height:193px" role="img" aria-label="Hands signing a mortgage document beside a small model house"></div>
  <div class="foot-brand">Quarry Lending</div>
</section>

<!-- Slide 3: what is mortgage servicing -->
<section class="slide col-l" style="top:1257px">
  <div class="brand-tag">Quarry Lending</div>
  <svg class="menu" viewBox="0 0 11 9"><path d="M0 1h11M0 4.5h11M0 8h11" stroke="#15284f" stroke-width="1"/></svg>
  <div class="photo warm" style="left:0;top:49px;width:198px;height:253px" role="img" aria-label="Woman reviewing paperwork at a desk"></div>
  <div class="abs" style="left:230px;top:62px;width:310px">
    <div class="kicker">Mortgage Servicing</div>
    <div class="title" style="font-size:18px"><span class="gold">What is</span> Mortgage Servicing?</div>
    <p class="body" style="margin-top:10px">Servicing covers payment collection, escrow management and borrower support across the full life of every loan we hold.</p>
  </div>
  <div class="abs navy on-dark" style="left:205px;top:160px;width:340px;height:115px;padding:18px 22px">
    <p class="body" style="width:140px">Clear processes that keep loans current and investors informed.</p>
    <div class="tick"><svg width="7" height="6" viewBox="0 0 7 6"><path d="M0.5 3l2 2 4-4.5" stroke="#36aaa2" stroke-width="1.3" fill="none"/></svg>Best Quality Home</div>
    <div class="tick"><svg width="7" height="6" viewBox="0 0 7 6"><path d="M0.5 3l2 2 4-4.5" stroke="#36aaa2" stroke-width="1.3" fill="none"/></svg>New Modern Home</div>
  </div>
  <div class="photo red" style="left:373px;top:160px;width:172px;height:115px" role="img" aria-label="Keys in the lock of a front door"></div>
  <div class="foot-brand">Quarry Lending</div>
</section>

<!-- Slide 4: key players -->
<section class="slide col-r" style="top:1257px">
  <div class="brand-tag">Quarry Lending</div>
  <div class="photo warm" style="left:348px;top:0;width:222px;height:272px" role="img" aria-label="Couple holding keys inside a new home"></div>
  <div class="abs navy" style="left:0;top:175px;width:460px;height:145px"></div>
  <div class="abs teal" style="left:334px;top:126px;width:24px;height:24px;display:flex;align-items:center;justify-content:center"><svg width="12" height="12" viewBox="0 0 12 12"><circle cx="6" cy="6" r="5" fill="none" stroke="#fff"/><path d="M3.5 6l1.8 1.8L8.5 4.5" stroke="#fff" fill="none"/></svg></div>
  <div class="abs" style="left:57px;top:86px">
    <div class="kicker">The Ecosystem</div>
    <div class="title"><span class="gold">Key Players in</span><br>Mortgage Servicing</div>
  </div>
  <div class="abs on-dark" style="left:57px;top:196px;width:230px">
    <div style="display:flex;gap:32px"><div class="stat" style="color:var(--gold)">+235<small>Description</small></div><div class="stat" style="color:var(--gold)">8,5%<small>Description</small></div></div>
    <p class="body" style="margin-top:14px">Originators, servicers, investors and regulators each play a role. Here we map how they connect and where value is created.</p>
  </div>
  <div class="foot-brand">Quarry Lending</div>
</section>

<!-- Slide 5: investment opportunities -->
<section class="slide col-l" style="top:1593px">
  <div class="abs navy" style="left:0;top:0;width:24px;height:294px"></div>
  <svg class="menu" viewBox="0 0 11 9"><path d="M0 1h11M0 4.5h11M0 8h11" stroke="#15284f" stroke-width="1"/></svg>
  <div class="photo sky" style="left:24px;top:0;width:260px;height:158px" role="img" aria-label="Modern apartment building against a blue sky"></div>
  <div class="photo red" style="left:24px;top:160px;width:162px;height:134px" role="img" aria-label="Keys hanging in a door lock"></div>
  <div class="abs" style="left:327px;top:92px;width:200px">
    <div class="kicker">Mortgage Servicing</div>
    <div class="title"><span class="gold">Investment</span><br>Opportunities</div>
    <p class="body" style="margin-top:10px">Servicing rights offer steady cash flow and a natural hedge within a broader fixed income portfolio.</p>
  </div>
  <div class="card" style="left:190px;top:198px;width:158px;height:64px;background:#fff;box-shadow:0 2px 8px rgba(0,0,0,.12);color:var(--muted)"><b style="color:var(--navy)">&#10003; Title here</b>Steady income from a diverse loan base.</div>
  <div class="card teal" style="left:354px;top:198px;width:155px;height:64px;color:#e9f7f6"><b style="color:#fff">&#10003; Title here</b>Long term value backed by real homes.</div>
  <div class="foot-brand">Quarry Lending</div>
</section>

<!-- Slide 6: types -->
<section class="slide col-r" style="top:1593px">
  <div class="brand-tag">Quarry Lending</div>
  <svg class="menu" viewBox="0 0 11 9"><path d="M0 1h11M0 4.5h11M0 8h11" stroke="#15284f" stroke-width="1"/></svg>
  <div class="photo desk" style="left:305px;top:0;width:265px;height:320px" role="img" aria-label="Model house on a desk beside a calculator and pen"></div>
  <div class="abs" style="left:57px;top:56px">
    <div class="kicker">Exploring Options</div>
    <div class="title"><span class="gold">Types of Mortgage</span><br>Servicing Investments</div>
  </div>
  <div class="abs navy on-dark" style="left:53px;top:159px;width:279px;height:99px;padding:14px 24px">
    <b style="font-size:7px;display:block;margin-bottom:5px">Description Here</b>
    <p class="body">Full servicing rights, excess servicing spreads and whole loan pools each carry their own balance of yield and risk for investors.</p>
  </div>
  <div class="abs teal" style="left:179px;top:251px;width:153px;height:21px;display:flex;align-items:center;gap:20px;padding-left:18px;color:#fff"><b style="font-size:10px">20%</b><span style="font-size:5.5px">Real Estate Information</span></div>
  <div class="foot-brand">Quarry Lending</div>
</section>

<!-- Slide 7: shaping the future -->
<section class="slide col-l" style="top:1927px">
  <div class="abs navy" style="left:0;top:0;width:24px;height:230px"></div>
  <svg class="menu" viewBox="0 0 11 9"><path d="M0 1h11M0 4.5h11M0 8h11" stroke="#15284f" stroke-width="1"/></svg>
  <div class="photo sky" style="left:24px;top:0;width:349px;height:229px" role="img" aria-label="City skyline with a rising blue arrow"></div>
  <div class="abs" style="left:398px;top:93px">
    <div class="kicker">Market Trends</div>
    <div class="title"><span class="gold">Shaping</span><br>the Future</div>
  </div>
  <p class="body abs" style="left:28px;top:250px;width:150px">Where servicing is heading and how we plan to stay ahead.</p>
  <div class="abs teal" style="left:200px;top:200px;width:194px;height:68px;padding:16px 22px;font-size:6.5px;line-height:1.6;color:#e9f7f6">Technology and data are changing how loans are serviced and valued.</div>
  <div class="abs navy" style="left:394px;top:200px;width:79px;height:68px;padding:16px 14px;color:#fff"><b style="font-size:11px;display:block">98%</b><span style="font-size:8px">&#9733;&#9733;&#9733;&#9733;&#9734;</span></div>
  <div class="foot-brand">Quarry Lending</div>
</section>

<!-- Slide 8: market trends -->
<section class="slide col-r" style="top:1927px">
  <div class="photo desk" style="left:0;top:0;width:570px;height:158px" role="img" aria-label="Hand holding a small model house while another hand signs papers"></div>
  <div class="abs navy on-dark" style="left:0;top:160px;width:244px;height:136px;padding:26px 52px 0 50px">
    <div class="kicker" style="color:#c9d0de">What Lies Ahead?</div>
    <div class="title"><span class="gold">Market Trends</span><br>and Outlook</div>
    <p class="body" style="margin-top:8px">Rates, home prices and demand shape the next cycle.</p>
  </div>
  <div class="abs" style="left:324px;top:226px;display:flex;gap:24px;color:var(--navy)">
    <div class="stat" style="font-size:12px">+3.900<small>Description</small></div>
    <div class="stat" style="font-size:12px">2024<small>Description</small></div>
    <div class="stat" style="font-size:12px">+80%<small>Description</small></div>
  </div>
  <div class="foot-brand">Quarry Lending</div>
</section>

<!-- Slide 9: risks -->
<section class="slide col-l" style="top:2262px">
  <div class="brand-tag">Quarry Lending</div>
  <svg class="menu" viewBox="0 0 11 9"><path d="M0 1h11M0 4.5h11M0 8h11" stroke="#15284f" stroke-width="1"/></svg>
  <div class="abs navy" style="left:0;top:260px;width:570px;height:60px"></div>
  <div class="photo" style="left:24px;top:50px;width:184px;height:175px;background:linear-gradient(140deg,#a6d6d3,#d7b58c)" role="img" aria-label="Hand stopping a row of falling wooden blocks"></div>
  <div class="abs" style="left:243px;top:52px">
    <div class="kicker">Real Estate Presentation Template</div>
    <div class="title"><span class="gold">Risks and</span><br>Mitigations</div>
  </div>
  <div class="card" style="left:24px;top:229px;width:234px;height:65px;background:#fff;box-shadow:0 2px 8px rgba(0,0,0,.12);color:var(--muted);padding:12px 14px 12px 44px">
    <svg class="abs" style="left:14px;top:14px" width="18" height="16" viewBox="0 0 18 16"><path d="M2 8L9 2l7 6M4 7v7h10V7" stroke="#36aaa2" stroke-width="1.4" fill="none"/></svg>
    Rate, credit and prepayment risk are managed with clear controls.<div class="stars" style="margin-top:4px">&#9733;&#9733;&#9733;&#9733;&#9733;</div>
  </div>
  <div class="photo warm" style="left:258px;top:146px;width:150px;height:148px" role="img" aria-label="Couple reviewing a chart on a tablet"></div>
  <div class="abs" style="left:437px;top:168px;width:110px">
    <b style="font-size:7px;color:var(--navy);display:block;margin-bottom:6px">Description Here</b>
    <p class="body">Regular stress tests and hedging keep the portfolio steady through shifting markets.</p>
  </div>
  <div class="foot-brand" style="color:#fff">Quarry Lending</div>
</section>

<!-- Slide 10: learning from the field -->
<section class="slide col-r" style="top:2262px">
  <div class="brand-tag">Hearthside Estate</div>
  <svg class="menu" viewBox="0 0 11 9"><path d="M0 1h11M0 4.5h11M0 8h11" stroke="#15284f" stroke-width="1"/></svg>
  <div class="abs navy on-dark" style="left:287px;top:50px;width:283px;height:93px;padding:30px 24px;display:flex;gap:40px">
    <b style="font-size:7px;white-space:nowrap">Description<br>Here</b>
    <p class="body">Real servicing cases show what works and what to avoid when building a strong portfolio.</p>
  </div>
  <div class="abs" style="left:58px;top:62px">
    <div class="kicker">Case Studies</div>
    <div class="title"><span class="gold">Learning from</span><br>The Field</div>
  </div>
  <div class="photo green" style="left:0;top:143px;width:444px;height:177px" role="img" aria-label="Hand holding house keys over a green field"></div>
  <div class="abs teal" style="left:394px;top:143px;width:100px;height:108px;padding:16px 12px;text-align:center;color:#fff">
    <b style="font-size:12px;display:block">$250,00</b>
    <b style="font-size:6px;display:block;margin:6px 0 3px">Description</b>
    <span style="font-size:6px;line-height:1.5;display:block">Average value per loan serviced</span>
  </div>
  <div class="foot-brand">Quarry Lending</div>
</section>

<!-- Slide 11: critical steps -->
<section class="slide col-l" style="top:2596px">
  <div class="brand-tag">Quarry Lending</div>
  <svg class="menu" viewBox="0 0 11 9"><path d="M0 1h11M0 4.5h11M0 8h11" stroke="#15284f" stroke-width="1"/></svg>
  <div class="abs navy" style="left:0;top:49px;width:304px;height:222px"></div>
  <div class="photo" style="left:24px;top:49px;width:126px;height:108px" role="img" aria-label="Team meeting around a table"></div>
  <div class="abs" style="left:98px;top:141px;background:var(--gold);color:var(--navy);font-size:6px;font-weight:700;padding:3px 12px">Title here</div>
  <div class="photo sky" style="left:24px;top:163px;width:126px;height:108px" role="img" aria-label="Waterfront city skyline"></div>
  <div class="abs" style="left:98px;top:256px;background:var(--gold);color:var(--navy);font-size:6px;font-weight:700;padding:3px 12px">Title here</div>
  <div class="photo" style="left:153px;top:49px;width:151px;height:222px" role="img" aria-label="Business handshake over a city backdrop"></div>
  <div class="abs" style="left:344px;top:90px;width:200px">
    <div class="kicker">The Importance of Due Diligence</div>
    <div class="title"><span class="gold">Critical Steps</span><br>For Investors</div>
    <div style="display:flex;align-items:center;gap:8px;margin:14px 0 10px;font-size:7px;font-weight:700;color:var(--navy)"><svg width="12" height="11" viewBox="0 0 12 11"><path d="M1 5.5L6 1l5 4.5M2.5 5v5h7V5" stroke="#36aaa2" fill="none"/></svg>Real Estate Market</div>
    <p class="body">Review loan quality, servicer history and local market data before committing capital to any servicing deal.</p>
  </div>
  <div class="foot-brand">Quarry Lending</div>
</section>

<!-- Slide 12: compliance -->
<section class="slide col-r" style="top:2596px">
  <div class="brand-tag">Quarry Lending</div>
  <div class="abs navy" style="left:179px;top:0;width:391px;height:320px"></div>
  <svg class="menu" viewBox="0 0 11 9"><path d="M0 1h11M0 4.5h11M0 8h11" stroke="#fff" stroke-width="1"/></svg>
  <div class="photo desk" style="left:79px;top:53px;width:243px;height:140px" role="img" aria-label="Small model houses on a desk with paperwork"></div>
  <div class="photo warm" style="left:327px;top:53px;width:243px;height:140px" role="img" aria-label="Couple meeting with an adviser"></div>
  <div class="abs teal" style="left:524px;top:176px;width:24px;height:24px;display:flex;align-items:center;justify-content:center"><svg width="12" height="11" viewBox="0 0 12 11"><path d="M1 5.5L6 1l5 4.5M2.5 5v5h7V5" stroke="#fff" fill="none"/></svg></div>
  <p class="body abs" style="left:42px;top:222px;width:120px">Every loan we service follows current federal and state rules.</p>
  <div class="abs on-dark" style="left:236px;top:222px">
    <div class="kicker" style="color:#c9d0de">Regulatory Landscape</div>
    <div class="title"><span class="gold">Navigating</span><br>Compliance</div>
  </div>
  <div class="foot-brand" style="color:#fff">Quarry Lending</div>
</section>

<!-- Slide 13: economic influencers -->
<section class="slide col-l" style="top:2932px">
  <div class="abs navy" style="left:344px;top:0;width:226px;height:320px"></div>
  <svg class="menu" viewBox="0 0 11 9"><path d="M0 1h11M0 4.5h11M0 8h11" stroke="#fff" stroke-width="1"/></svg>
  <div class="photo red" style="left:60px;top:0;width:284px;height:158px" role="img" aria-label="Model house with a rising market chart behind it"></div>
  <div class="abs on-dark" style="left:380px;top:58px;width:160px;text-align:center">
    <svg width="14" height="14" viewBox="0 0 14 14"><circle cx="9" cy="5" r="3.5" fill="none" stroke="#d6a534" stroke-width="1.3"/><path d="M6.5 7.5L1.5 12.5M3 11l1.5 1.5" stroke="#d6a534" stroke-width="1.3"/></svg>
    <b style="display:block;font-size:7px;color:var(--gold);margin:6px 0">Description Here</b>
    <p class="body">Interest rates and jobs data drive prepayment speeds and value.</p>
  </div>
  <div class="photo" style="left:373px;top:158px;width:129px;height:129px;background:linear-gradient(140deg,#eef1ee,#c9bfae)" role="img" aria-label="Small white and red model houses"></div>
  <div class="abs" style="left:60px;top:200px">
    <div class="kicker">Impact of Economic Factors</div>
    <div class="title"><span class="gold">Economic</span> Influencers</div>
  </div>
  <div class="abs" style="left:60px;top:252px;display:flex;gap:20px;width:260px">
    <b style="font-size:6px;color:var(--gold)">Description<br>Here</b>
    <p class="body">Inflation, wages and housing supply all shape how borrowers pay over time.</p>
  </div>
  <div class="foot-brand">Quarry Lending</div>
</section>

<!-- Slide 14: what we service -->
<section class="slide col-r" style="top:2932px">
  <div class="abs navy" style="left:0;top:0;width:208px;height:320px"></div>
  <div class="brand-tag on-navy">Quarry Lending</div>
  <div class="abs on-dark" style="left:38px;top:108px;width:150px">
    <div class="kicker" style="color:#c9d0de">Real Estate Presentation Template</div>
    <div class="title"><span class="gold">What We</span><br>Service ?</div>
    <p class="body" style="margin-top:10px">Full servicing support from first payment to final payoff.</p>
  </div>
  <div class="svc-ico" style="top:43px"><svg width="12" height="12" viewBox="0 0 12 12"><path d="M3 1l2 3-1.5 1.5a7 7 0 003 3L8 7l3 2-1 2C5 11 1 7 1 2z" fill="#fff"/></svg></div>
  <div class="svc" style="top:43px"><b>Our Service 01</b><p class="body">Payment processing and account setup for every new loan.</p></div>
  <div class="svc-ico" style="top:107px"><svg width="12" height="12" viewBox="0 0 12 12"><circle cx="5" cy="5" r="3.5" fill="none" stroke="#fff" stroke-width="1.3"/><path d="M7.5 7.5L11 11" stroke="#fff" stroke-width="1.3"/></svg></div>
  <div class="svc" style="top:107px"><b>Our Service 02</b><p class="body">Escrow review for taxes and insurance each year.</p></div>
  <div class="svc-ico" style="top:172px"><svg width="12" height="12" viewBox="0 0 12 12"><circle cx="6" cy="3" r="2" fill="#fff"/><circle cx="2.5" cy="9" r="2" fill="#fff"/><circle cx="9.5" cy="9" r="2" fill="#fff"/></svg></div>
  <div class="svc" style="top:172px"><b>Our Service 03</b><p class="body">Borrower support and loss mitigation when help is needed.</p></div>
  <div class="svc-ico" style="top:236px"><svg width="12" height="12" viewBox="0 0 12 12"><rect x="2.5" y="5" width="7" height="6" fill="#fff"/><path d="M4 5V3.5a2 2 0 014 0V5" stroke="#fff" fill="none"/></svg></div>
  <div class="svc" style="top:236px"><b>Our Service 04</b><p class="body">Investor reporting with clear monthly performance data.</p></div>
  <div class="photo desk" style="left:401px;top:0;width:169px;height:320px" role="img" aria-label="Hand holding a small dark model house"></div>
</section>

<!-- Slide 15: thanks -->
<section class="slide col-l" style="top:3267px">
  <div class="brand-tag">Hearthside Estate</div>
  <svg class="menu" viewBox="0 0 11 9"><path d="M0 1h11M0 4.5h11M0 8h11" stroke="#15284f" stroke-width="1"/></svg>
  <div class="abs navy" style="left:301px;top:129px;width:269px;height:191px"></div>
  <div class="photo desk" style="left:251px;top:50px;width:251px;height:222px" role="img" aria-label="Calculator with a refinance display"></div>
  <div class="abs" style="left:57px;top:86px">
    <div class="kicker">Real Estate Presentation Template</div>
    <div class="title" style="font-size:38px;font-weight:900">Thanks</div>
  </div>
  <div class="abs teal" style="left:24px;top:150px;width:24px;height:122px"></div>
  <div class="abs" style="left:48px;top:150px;width:203px;height:122px;background:#fff;padding:14px 16px;box-shadow:0 2px 8px rgba(0,0,0,.08)">
    <div class="contact"><svg width="9" height="9" viewBox="0 0 12 12"><path d="M3 1l2 3-1.5 1.5a7 7 0 003 3L8 7l3 2-1 2C5 11 1 7 1 2z" fill="#d6a534"/></svg><div><b>Telephone :</b><span>0912 - 555 0148</span></div></div>
    <div class="contact"><svg width="9" height="9" viewBox="0 0 12 12"><path d="M1 6L6 1.5 11 6M2.5 5.5V11h7V5.5" stroke="#d6a534" stroke-width="1.4" fill="none"/></svg><div><b>Address :</b><span>2150 Harbor Street City</span></div></div>
    <div class="contact"><svg width="9" height="9" viewBox="0 0 12 12"><rect x="1" y="2.5" width="10" height="7" fill="none" stroke="#d6a534" stroke-width="1.3"/><path d="M1 2.5l5 4 5-4" stroke="#d6a534" fill="none"/></svg><div><b>Email :</b><span>hello@hearthside-estate.com</span></div></div>
  </div>
</section>

</body>
</html>
```